Vornel Technologies business card design

We need a business card designed with our new logo. it would be great if the card could communicate it is a technology based company.

Target Market(s)

system integrators

Industry/Entity Type

technology, IOT

Contact Information for Business Card

Name, designation, Address, telephone number, email address

Requirements
Must have
• logo and company name
Nice to have
• something to do with technology

```html
<!DOCTYPE html>
<html lang="en">
<head>
<meta charset="utf-8">
<title>Vornel Technologies business card</title>
<link href="https://fonts.googleapis.com/css2?family=Exo+2:wght@600&family=Roboto+Condensed:wght@400&display=swap" rel="stylesheet">
<style>
  :root {
    --page-bg: #e4e4e4;
    --card-top: #49484c;
    --card-bottom: #39383c;
    --accent: #e8891c;
    --text-light: #f2f2f2;
    --mark-grey: #6a696d;
  }
  * { margin: 0; padding: 0; box-sizing: border-box; }
  html, body {
    width: 1200px;
    height: 1200px;
    overflow: hidden;
    background: var(--page-bg);
  }
  .canvas {
    position: relative;
    width: 1200px;
    height: 1200px;
  }
  .card {
    position: absolute;
    left: 257px;
    width: 686px;
    height: 392px;
    border-radius: 26px;
    background: linear-gradient(180deg, var(--card-top), var(--card-bottom));
    overflow: hidden;
  }
  .card--front { top: 165px; }
  .card--back { top: 653px; }

  .contact-block {
    position: absolute;
    left: 55px;
    top: 138px;
    color: var(--text-light);
    font-family: "Roboto Condensed", sans-serif;
    font-size: 17px;
    line-height: 21px;
  }
  .person-name {
    font-family: "Exo 2", sans-serif;
    font-weight: 600;
    font-size: 25px;
    line-height: 28px;
    color: var(--accent);
    letter-spacing: 0.3px;
  }
  .person-title { margin-top: 1px; }
  .address { margin-top: 14px; }
  .contact-list {
    list-style: none;
    margin-top: 14px;
  }
  .contact-list li {
    display: flex;
    align-items: center;
    gap: 9px;
    height: 21.5px;
  }
  .contact-icon {
    width: 14px;
    height: 14px;
    flex: none;
    fill: var(--accent);
  }

  .brand-lockup {
    position: absolute;
    left: 0;
    right: 0;
    top: 50%;
    transform: translateY(-50%);
    display: flex;
    align-items: center;
    justify-content: center;
    gap: 16px;
  }
  .brand-square {
    width: 34px;
    height: 34px;
    background: var(--mark-grey);
  }
  .brand-name {
    font-family: "Exo 2", sans-serif;
    font-weight: 600;
    font-size: 38px;
    letter-spacing: 3px;
    color: var(--mark-grey);
    text-transform: uppercase;
  }
</style>
</head>
<body>
<main class="canvas">

  <section class="card card--front">
    <div class="contact-block">
      <h1 class="person-name">Daniel Marsh</h1>
      <p class="person-title">Managing Director</p>
      <p class="address">4120 Larchmont Road<br>Fairbanks, Alaska 99709</p>
      <ul class="contact-list">
        <li>
          <svg class="contact-icon" viewBox="0 0 16 16" aria-hidden="true"><path d="M3.2 1.2 5.6 1l1.3 3.3-1.6 1.2a8 8 0 0 0 5 5l1.2-1.6 3.3 1.3-.2 2.4c-.1.9-.9 1.5-1.8 1.4C6.5 13.4 2.6 9.5 1.8 3c-.1-.9.5-1.7 1.4-1.8z"/></svg>
          <span>555-214-7730</span>
        </li>
        <li>
          <svg class="contact-icon" viewBox="0 0 16 16" aria-hidden="true"><path d="M4.5 0h7A1.5 1.5 0 0 1 13 1.5v13a1.5 1.5 0 0 1-1.5 1.5h-7A1.5 1.5 0 0 1 3 14.5v-13A1.5 1.5 0 0 1 4.5 0zM5 2v10h6V2zm3 11a1 1 0 1 0 0 2 1 1 0 0 0 0-2z"/></svg>
          <span>555-380-1946</span>
        </li>
        <li>
          <svg class="contact-icon" viewBox="0 0 16 16" aria-hidden="true"><path d="M1 3h14v10H1zm1.5 1.2v.3L8 8.3l5.5-3.8v-.3zm0 2.1v5.5h11V6.3L8 10.1z"/></svg>
          <span>info@vornel.com</span>
        </li>
        <li>
          <svg class="contact-icon" viewBox="0 0 16 16" aria-hidden="true"><path d="M8 1a7 7 0 1 0 0 14A7 7 0 0 0 8 1zm-1 2.2c.6.8.3 1.6-.5 2.1-.9.6-.6 1.6.4 1.8 1.2.2 1.6 1.3 1 2.3-.5.8-.3 2 .5 2.8A5 5 0 0 1 3.3 6c.9.2 1.6-.3 1.8-1.1.2-.7.9-1.4 1.9-1.7zm4.4 1.6a5 5 0 0 1 1.5 4.9c-.8-.6-1.9-.5-2.4-1.4-.4-.8.2-1.6 0-2.5-.1-.5.3-.9.9-1z"/></svg>
          <span>www.vornel.com</span>
        </li>
      </ul>
    </div>
  </section>

  <section class="card card--back">
    <div class="brand-lockup">
      <span class="brand-square" aria-hidden="true"></span>
      <span class="brand-name">Vornel Technologies</span>
    </div>
  </section>

</main>
</body>
</html>
```